Chinese citizens moving to SYDNEY!

We need an A5 size flier for our new business. We would like this to be a fold-out flyer (brochure-style, i.e. 4 sides - front cover, middle, back cover). Full colour print (or 4 colour if it can be done without compromising the look). We need two versions of the same flyer - one in Chinese and one in English. Same design and imagery, just different languages. Copy is attached with imagery (subject to change once we source high res images).

Target Market(s)

Chinese citizens looking to emigrate to Sydney AND Chinese citizens who have recently moved to Sydney.

Industry/Entity Type

Business

Font styles to use
Sans Serif

Colors
ec1f27
000000
ffffff
fece3e

Requirements
Must have
• The front cover of the flier must be clean looking and show just our business name and tag line, along with an image of Sydney Harbour (provided). Main information ideally to be spread across the 2 centre pages with the back page quite clean, but if the text is too small we could consider it being spread across the remaining 3 pages (i.e. centre of the brochure, then the back cover).
• We would like it to be a clean and easy to read design. Suggested colours are written in the brief.
• It would be ideal to have a designer who can read Mandarin so that they know which characters make up a headline, which characters should not be spaced over two rows of text etc.

```html
<!DOCTYPE html>
<html lang="en">
<head>
<meta charset="utf-8">
<title>Harbour Gate Concierge – Services Flyer</title>
<link href="https://fonts.googleapis.com/css2?family=Source+Sans+3:wght@400;600;700&display=swap" rel="stylesheet">
<style>
  :root {
    --brand-red: #d8232a;
    --text-light: #ffffff;
    --photo-sky: #8fb3cf;
    --photo-navy: #35424f;
    --photo-house: #b9b2a4;
    --photo-dusk: #4d5a6b;
    --photo-produce: #b5562f;
    --photo-green: #6f8f3a;
    --photo-beach: #9cc4de;
    --photo-sand: #d9c3a2;
  }
  * { margin: 0; padding: 0; box-sizing: border-box; }
  html, body { width: 847px; height: 1200px; overflow: hidden; }
  body {
    position: relative;
    background: var(--brand-red);
    color: var(--text-light);
    font-family: "Source Sans 3", "Helvetica Neue", Arial, sans-serif;
  }
  .flyer-header { position: absolute; top: 24px; left: 0; width: 847px; text-align: center; }
  .brand-name { font-size: 41px; font-weight: 700; line-height: 46px; }
  .tagline { font-size: 22.3px; font-weight: 700; line-height: 23.5px; }
  .intro { margin-top: 9px; font-size: 16.2px; line-height: 17.3px; }
  .intro p { margin-bottom: 8.6px; }

  .services-title {
    position: absolute; top: 329px; left: 31px;
    font-size: 24px; font-weight: 700; line-height: 28px;
  }
  .section-heading {
    position: absolute; left: 32px;
    font-size: 20px; font-weight: 700; line-height: 24px;
  }
  .section-photo {
    position: absolute; left: 0; width: 231px;
    border-radius: 0 115px 115px 0 / 0 50% 50% 0;
  }
  .photo-school  { top: 397px; height: 170px; background: linear-gradient(160deg, var(--photo-sky), var(--photo-navy) 70%); }
  .photo-home    { top: 602px; height: 169px; background: linear-gradient(170deg, var(--photo-dusk), var(--photo-house) 55%, #3a3a38); }
  .photo-grocery { top: 803px; height: 180px; background: linear-gradient(175deg, #6a5a4a, var(--photo-produce) 55%, var(--photo-green)); }
  .photo-family  { top: 1024px; height: 176px; background: linear-gradient(180deg, var(--photo-beach), #e9eef2 55%, var(--photo-sand)); }

  .service-list {
    position: absolute; left: 239px; width: 600px;
    list-style: none; font-size: 15.9px; line-height: 17.2px;
  }
  .service-list li { white-space: nowrap; }
  .service-list li::before { content: "•"; }
  .service-list li.continued::before { content: ""; }
  .list-school   { top: 392px; }
  .list-home     { top: 599px; line-height: 20.3px; }
  .list-everyday { top: 801px; }
  .list-health   { top: 1019px; }
</style>
</head>
<body>
  <header class="flyer-header">
    <h1 class="brand-name">Harbour Gate Concierge</h1>
    <p class="tagline">is a premium lifestyle service supporting families<br>who are planning or currently migrating to and investing in Australia.</p>
    <div class="intro">
      <p>Specialising in the city of Sydney, Harbour Gate Concierge<br>helps families to feel comfortable and at home as soon as possible.</p>
      <p>Our team of local experts provide support every step of the way<br>– answering questions, providing advice and breaking down the language barrier.</p>
      <p>Our services are highly customisable to suit the needs of individual families.<br>Whether it’s finding the best school for your children, the help you need in your home, knowing where to buy your<br>favourite groceries or an introduction to a great GP or Specialist<br>– Harbour Gate Concierge will cater to your every need.</p>
      <p>Your family will be assigned a professional Personal Assistant who is fluent in both English and Mandarin,<br>making the process of migrating less daunting and more enjoyable.</p>
    </div>
  </header>

  <h2 class="services-title">Our services include but are not limited to:</h2>

  <h3 class="section-heading" style="top:369px">School</h3>
  <div class="section-photo photo-school" role="img" aria-label="Photo of schoolchildren in uniform walking with folders"></div>
  <ul class="service-list list-school">
    <li>Recommend the best schools and childcare centres</li>
    <li>Compare school rankings and academic results</li>
    <li>Arrange private tours of schools and meetings with Principals</li>
    <li>Manage the school application process through to completion</li>
    <li>Assist with starting school, such as purchase of uniforms and textbooks,<br>understanding school procedures and more</li>
    <li>Appoint private tutors to assist with learning English and completing homework<br>assignments</li>
    <li>Organise extra curricular activities, such as piano lessons, tennis lessons and more</li>
    <li>Translate all school correspondence such as academic report cards, homework<br>assignments and more</li>
  </ul>

  <h3 class="section-heading" style="top:575px">Home &amp; Car</h3>
  <div class="section-photo photo-home" role="img" aria-label="Photo of a family home at dusk with a car in the driveway"></div>
  <ul class="service-list list-home">
    <li>Recommend the best suburbs for families</li>
    <li>Make introductions to Real Estate Agents and support the buying process</li>
    <li>Arrange unpacking and home organisation services</li>
    <li>Assist to purchase furniture and appliances</li>
    <li>Source the best utility companies and organise connection</li>
    <li class="continued">– electricity, gas, water, phone, internet, TV and more</li>
    <li>Appoint staff for your home such as cleaners, gardeners and more</li>
    <li>Compare home insurance options and assist with purchasing</li>
    <li>Assist with car purchasing, leasing and acquiring necessary insurance</li>
  </ul>

  <h3 class="section-heading" style="top:779px">Everyday Necessities</h3>
  <div class="section-photo photo-grocery" role="img" aria-label="Photo of fresh fruit and produce in a grocery store"></div>
  <ul class="service-list list-everyday">
    <li>Explain local grocery options such as supermarkets, specialty stores,<br>Asian grocers and more</li>
    <li>Recommend beauty and wellness services such as hair salons, nail parlours,<br>beauty salons and more</li>
    <li>Explain retail shopping options such major shopping centres and luxury brands</li>
    <li>Source quality trades people such as plumbers, electricians, painters and more</li>
    <li>Assist with government registrations such as drivers license, Medicare and more</li>
    <li>Assist to open bank accounts and set up online banking</li>
    <li>Assist to set up memberships – library, gym, golf club and more</li>
    <li>Explain private and public transport options</li>
    <li>Organise private and group language classes</li>
    <li>Translate documents and mail</li>
  </ul>

  <h3 class="section-heading" style="top:997px">Health &amp; Lifestyle</h3>
  <div class="section-photo photo-family" role="img" aria-label="Photo of a happy family at the beach"></div>
  <ul class="service-list list-health">
    <li>Compare health insurance options</li>
    <li>Recommend the best medical professionals</li>
    <li class="continued">– GP, Dentist, Acupuncture and more</li>
    <li>Recommend restaurants</li>
    <li>Suggest the best local parks to visit and other outdoor activities</li>
    <li>Explain local dangers such as Australian wildlife, beach safety and more</li>
    <li>Suggest family outings, recommend holiday destinations, plan children’s birthday<br>parties, play dates and more</li>
    <li>Arrange Private chauffers</li>
  </ul>
</body>
</html>
```